Design a Striking Charity Infographic for the Displaced Meal Pledge

Design a striking infographic to share online and raise awareness of the Meal Pledge.

This is a charity project that raises funds to provide refugees with the food, medicine and support they need to survive.

Your design should include the text and ingredients outlined below.

The infographic should be a strong visual statement that’s easy to share on social media such as Snapgrid, Chirpline and Friendwall.

The headline, ingredients and call to action 'Take the Kind Harbor Meal Pledge, June 19-25'

Text:
Headline: “Could you live on this much food for 1 week?”
Rice 1920g
Flour 400g
Lentils 170g
Dried chick peas 85g
Tinned sardines 125g
Tinned kidney beans 400g
Vegetable Oil 300ml

Take the Kind Harbor Meal Pledge, June 19-25
Sign up at www.mealpledgeweek.org.au
(this section with the web address needs to be very clear and easy to see in the graphic)

Footer text - note this section should not dominate, it's a teriary section of the design.
(1) Kind Harbor / Meal Pledge logo
(2) Design by PixelGuild (logo attached)

This copy needs to appear somewhere (very small) “The international aid agency of the Federated Assembly of Parishes. ABN 17 826 305 462”

Technical spec:
Imagery: photos are permitted; custom illustrations encouraged!
Size: maximum 1080x1080px
File size smaller than 5 MB
Colour ratios: Blue and White (80%), tertiary is red; see guide for more details

If the main image is full bleed you can stick headline copy, logos etc on top of it. Put body copy on a grunge brush.

If the images are not full bleed, use a blue background image (rice bag or paper) for the background. Put all the images in a frame. And fasten them on with a fastener (e.g. staple). Make the proportions of the frames / backgrounds / fasteners look realistic.

Logo:
Use the Meal Pledge stamp (larger) and Kind Harbor logo (smaller) on everything. Unless it’s on a plain white background use the sicker version of the KH logo.

Typography:
Veneer 2 for headlines
Caecelia is for body copy in print / on posters / on images put headline and body copy on a grunge brush
Remington Noiseless - use sparingly for personality elements, not for body copy

Pls read the Meal Pledge Visual identity guidelines attached

Background:
From the organizers: "The numbers of refugees are hard to get your head around. And that’s why you taking this challenge is so important.

By putting yourself in the shoes of just one refugee, for just one week, you’re helping to communicate the suffering caused by this crisis on a human level. At a level we, and those around us, can actually understand."

Extra assets:

Frames and fasteners and other assets can be found here: https://files.vaultdrop.example/s/q4m8zt2lwn5rkx0bc3yhd7pfe916gvja

Requirements
Must have
• Refer to the attached visual design guidelines pdf got the colour ratios

```html
<!DOCTYPE html>
<html lang="en">
<head>
<meta charset="utf-8">
<title>Kind Harbor Meal Pledge – Could you live on this much food for 1 week?</title>
<link rel="stylesheet" href="https://fonts.googleapis.com/css2?family=Bebas+Neue&family=Roboto+Condensed:wght@700&family=Open+Sans:wght@400;600;700&display=swap">
<style>
  :root {
    --blue: #1d5f86;
    --blue-dark: #174e70;
    --red: #8e2430;
    --ink: #1c1c1c;
    --paper: #e9e1d6;
    --paper-light: #efe9e1;
    --frame: #f6f5f3;
    --bag: #b9c2c7;
    --tape: rgba(238, 233, 210, 0.85);
    --white: #ffffff;
  }
  * { margin: 0; padding: 0; box-sizing: border-box; }
  html, body { width: 1200px; height: 1200px; overflow: hidden; }
  body { background: var(--bag); font-family: "Open Sans", sans-serif; }

  .poster { position: relative; width: 1200px; height: 1200px; overflow: hidden;
    background: linear-gradient(135deg, #c4ccd0 0%, #aeb8be 50%, #c7cbc9 100%); }

  .bag-texture { position: absolute; inset: 0;
    background: linear-gradient(160deg, #c9ced0, #a9b3b9 60%, #bcc3c6); }

  .paper { position: absolute; left: 44px; top: 28px; width: 1117px; height: 1150px;
    background: linear-gradient(150deg, var(--paper-light) 0%, var(--paper) 55%, #ddd4c7 100%);
    box-shadow: 0 3px 10px rgba(0,0,0,.25); }

  .bolt { position: absolute; width: 34px; height: 34px; border-radius: 50%;
    background: radial-gradient(circle at 35% 30%, #fafafa 0%, #b8b8b8 45%, #555 100%);
    box-shadow: 0 2px 4px rgba(0,0,0,.45); }

  .stamp { position: absolute; background: #d8cfbf; opacity: .75; }
  .tape { position: absolute; background: var(--tape); box-shadow: 0 1px 2px rgba(0,0,0,.1); }

  .headline { position: absolute; left: 244px; top: 39px; width: 712px; height: 140px;
    background: var(--blue); transform: rotate(-0.6deg);
    font-family: "Bebas Neue", sans-serif; color: var(--white); text-align: center;
    line-height: .95; padding-top: 12px; }
  .headline .line { display: block; font-size: 68px; letter-spacing: 1px; }
  .headline .big { font-size: 84px; }

  .frame { position: absolute; left: 194px; top: 233px; width: 826px; height: 667px;
    background: var(--frame); box-shadow: 0 4px 10px rgba(0,0,0,.25); }
  .frame-inner { position: absolute; left: 39px; top: 45px; width: 748px; height: 566px;
    background: linear-gradient(160deg, #ebe4da, #e2d9cc); }

  .pledge-title { position: absolute; left: 0; top: 0; width: 826px; text-align: center;
    font-family: "Roboto Condensed", sans-serif; font-size: 31px; line-height: 44px;
    color: var(--blue); letter-spacing: .5px; }
  .pledge-title .lead { color: var(--red); font-weight: 400; }

  .item { position: absolute; font-family: "Bebas Neue", sans-serif; line-height: .9; }
  .item .name { display: block; color: var(--ink); font-size: 36px; }
  .item .qty { display: block; color: var(--red); font-size: 36px; }
  .item svg { position: absolute; }

  .cause { position: absolute; left: 500px; top: 633px; width: 456px; height: 165px;
    background: var(--red); font-family: "Bebas Neue", sans-serif; color: var(--white);
    font-size: 48px; line-height: 1.08; padding: 14px 20px 0 38px; }
  .cause .hl { background: var(--blue); padding: 0 4px; }

  .dates { position: absolute; left: 194px; top: 848px; width: 826px; text-align: center;
    font-family: "Open Sans", sans-serif; font-weight: 700; font-size: 42px; color: var(--blue); }

  .signup { position: absolute; left: 389px; top: 931px; width: 420px; height: 130px;
    background: var(--red); color: var(--white); text-align: center; transform: rotate(-0.4deg); }
  .signup .cta { display: block; font-family: "Bebas Neue", sans-serif; font-size: 96px;
    line-height: 1; padding-top: 8px; letter-spacing: 1px; }
  .signup .url { display: block; font-family: "Roboto Condensed", sans-serif; font-size: 25px;
    line-height: 1; margin-top: -4px; }

  .brand-mark { position: absolute; left: 98px; top: 1031px; width: 122px; height: 120px;
    display: flex; align-items: center; gap: 6px; }
  .brand-mark .square { width: 14px; height: 14px; background: var(--blue); flex: none; }
  .brand-mark .name { font-family: "Bebas Neue", sans-serif; font-size: 26px; line-height: .95;
    color: var(--blue); }

  .stamp-mark { position: absolute; left: 1020px; top: 1027px; width: 104px; height: 104px;
    display: flex; flex-direction: column; align-items: center; justify-content: center; }
  .stamp-mark .circle { width: 20px; height: 20px; border-radius: 50%; background: var(--blue); margin-bottom: 6px; }
  .stamp-mark .name { font-family: "Bebas Neue", sans-serif; font-size: 22px; color: var(--blue); text-align: center; line-height: 1; }

  .credit { position: absolute; left: 500px; top: 1088px; width: 200px; display: flex;
    align-items: center; justify-content: center; gap: 7px;
    font-family: "Open Sans", sans-serif; font-weight: 600; font-size: 21px; color: #2b3b4a; }
  .credit .circle { width: 16px; height: 16px; border-radius: 50%; background: var(--blue); }

  .legal { position: absolute; left: 0; top: 1128px; width: 1200px; text-align: center;
    font-size: 12.5px; color: var(--ink); }
</style>
</head>
<body>
<main class="poster">
  <div class="bag-texture" role="img" aria-label="Printed rice sack texture in soft blue grey"></div>

  <section class="paper">
    <div class="stamp" style="left:58px;top:56px;width:110px;height:160px;" role="img" aria-label="Faded ration stamp"></div>
    <div class="stamp" style="left:950px;top:588px;width:112px;height:240px;" role="img" aria-label="Faded ration points stamp"></div>
    <div class="stamp" style="left:180px;top:760px;width:120px;height:120px;" role="img" aria-label="Faded ration stamp"></div>
  </section>

  <span class="bolt" style="left:44px;top:55px;"></span>
  <span class="bolt" style="left:1105px;top:55px;"></span>
  <span class="bolt" style="left:33px;top:1117px;"></span>
  <span class="bolt" style="left:1118px;top:1128px;"></span>

  <div class="frame">
    <div class="frame-inner"></div>
    <h2 class="pledge-title"><span class="lead">TAKE THE </span>KIND HARBOR MEAL PLEDGE</h2>
  </div>

  <div class="tape" style="left:930px;top:185px;width:200px;height:52px;transform:rotate(32deg);"></div>
  <div class="tape" style="left:80px;top:790px;width:230px;height:56px;transform:rotate(40deg);"></div>
  <div class="tape" style="left:918px;top:298px;width:200px;height:44px;transform:rotate(38deg);opacity:.7;"></div>

  <h1 class="headline">
    <span class="line">Could you live on this</span>
    <span class="line">much food for <span class="big">1 week?</span></span>
  </h1>

  <!-- ration items -->
  <div class="item" style="left:276px;top:344px;">
    <span class="name">Rice</span><span class="qty">1920g</span>
  </div>
  <svg style="position:absolute;left:378px;top:311px;" width="72" height="118" viewBox="0 0 72 118">
    <rect x="0" y="0" width="72" height="118" rx="3" fill="var(--blue)"/>
    <rect x="0" y="8" width="72" height="3" fill="var(--blue-dark)"/>
    <rect x="0" y="107" width="72" height="3" fill="var(--blue-dark)"/>
    <rect x="14" y="28" width="44" height="62" fill="var(--white)"/>
  </svg>

  <div class="item" style="left:524px;top:344px;">
    <span class="name">Flour</span><span class="qty">400g</span>
  </div>
  <svg style="position:absolute;left:620px;top:342px;" width="60" height="78" viewBox="0 0 60 78">
    <rect x="0" y="0" width="60" height="78" rx="3" fill="var(--blue)"/>
    <rect x="12" y="16" width="36" height="44" fill="var(--white)"/>
  </svg>

  <div class="item" style="left:774px;top:317px;">
    <span class="name">Tinned<br>Kidney<br>Beans</span><span class="qty">400g</span>
  </div>
  <svg style="position:absolute;left:884px;top:336px;" width="50" height="82" viewBox="0 0 50 82">
    <rect x="0" y="0" width="50" height="82" rx="3" fill="var(--blue)"/>
    <path d="M0 22 Q25 14 50 22 L50 60 Q25 52 0 60 Z" fill="var(--white)"/>
  </svg>

  <div class="item" style="left:258px;top:489px;">
    <span class="name">Vegetable Oil</span><span class="qty">300ml</span>
  </div>
  <svg style="position:absolute;left:372px;top:526px;" width="100" height="46" viewBox="0 0 100 46">
    <path d="M0 4 Q0 0 4 0 H78 L88 10 H100 V36 H88 L78 46 H4 Q0 46 0 42 Z" fill="var(--blue)"/>
    <rect x="12" y="16" width="42" height="30" fill="var(--white)"/>
  </svg>

  <div class="item" style="left:524px;top:489px;">
    <span class="name">Tinned<br>Sardines</span><span class="qty">125g</span>
  </div>
  <svg style="position:absolute;left:662px;top:517px;" width="78" height="44" viewBox="0 0 78 44">
    <rect x="0" y="0" width="78" height="44" rx="2" fill="var(--blue)"/>
    <rect x="0" y="8" width="72" height="14" fill="var(--white)"/>
  </svg>

  <div class="item" style="left:774px;top:489px;">
    <span class="name">Lentils</span><span class="qty">170g</span>
  </div>
  <svg style="position:absolute;left:884px;top:496px;" width="78" height="102" viewBox="0 0 78 102">
    <rect x="0" y="0" width="78" height="102" rx="3" fill="var(--blue)"/>
    <rect x="0" y="7" width="78" height="3" fill="var(--blue-dark)"/>
    <rect x="16" y="26" width="46" height="54" fill="var(--white)"/>
  </svg>

  <div class="item" style="left:258px;top:622px;">
    <span class="name">Dried<br>Chick<br>Peas</span><span class="qty">85g</span>
  </div>
  <svg style="position:absolute;left:372px;top:622px;" width="80" height="112" viewBox="0 0 80 112">
    <rect x="0" y="0" width="80" height="112" rx="3" fill="var(--blue)"/>
    <rect x="0" y="8" width="80" height="3" fill="var(--blue-dark)"/>
    <rect x="17" y="28" width="46" height="58" fill="var(--white)"/>
  </svg>

  <p class="cause">
    This <span class="hl">7 day ration</span> will
    <span class="hl">raise money</span> to <span class="hl">help</span>
    <span class="hl">refugees</span> worldwide.
  </p>

  <p class="dates">JUNE 19-25, 2016</p>

  <a class="signup">
    <span class="cta">Sign up at</span>
    <span class="url">WWW.MEALPLEDGEWEEK.ORG.AU</span>
  </a>

  <div class="brand-mark">
    <span class="square"></span>
    <span class="name">Kind Harbor<br>Meal Pledge</span>
  </div>

  <div class="stamp-mark">
    <span class="circle"></span>
    <span class="name">Meal<br>Pledge</span>
  </div>

  <div class="credit"><span class="circle"></span>PixelGuild</div>

  <p class="legal">The international aid agency of the Federated Assembly of Parishes. ABN 17 826 305 462</p>
</main>
</body>
</html>
```